Stylish Business Card for Modern hair salon

I need a simple business card design using our salon logo and colours that are in the logo. We service clients of all ages but predominantly those in the 18 to 55 age range. We have a young staff and are looking to have a card that will present a modern and clean image that represents who we are. The card should be in black and white same as our logo. Minimal use of other colours is allowed.

Industry/Entity Type

Hair And Beauty

Contact Information for Business Card

The design should have the following information
salon name - TR Hair Studio
address - 2751 Birchfield Rd.E. Mississauga, ON L7P3K2
phone - 905 614-2870
website - trhairexample.ca
instagram - tr.hairstudio
twitter - @TR_HairStudio

Colors
000000
ffffff
474747

Requirements
Must have
• simple design, salon name, address, phone, website, instagram, twitter info
• Back of card should have the following:
• YOUR NEXT APPOINTMENT
• DATE
• TIME
Nice to have
• simple design, clear to see and read,
• predominantly black and white colour, minimal use of other colours is ok
Should not have
• many colours, various fonts

```html
<!DOCTYPE html>
<html lang="en">
<head>
<meta charset="utf-8">
<title>TR Hair Studio – Business Card</title>
<link rel="stylesheet" href="https://fonts.googleapis.com/css2?family=Montserrat:wght@400;500&display=swap">
<style>
  :root {
    --stage: #eaebed;
    --ink: #070808;
    --paper: #ffffff;
    --grey: #474747;
  }
  * { box-sizing: border-box; margin: 0; padding: 0; }
  html, body {
    width: 1200px; height: 1200px; overflow: hidden;
    background: var(--stage);
    font-family: "Montserrat", Arial, sans-serif;
  }
  .canvas { position: relative; width: 1200px; height: 1200px; }

  .card { position: absolute; border-radius: 20px; overflow: hidden; }

  .card-front {
    left: 312px; top: 211px; width: 588px; height: 387px;
    background: var(--ink);
  }
  .front-name {
    position: absolute; left: 0; right: 0; top: 170px;
    text-align: center;
    color: var(--paper);
    font-weight: 500;
    font-size: 48px;
    line-height: 56px;
    letter-spacing: 2px;
    text-transform: uppercase;
  }

  .card-back {
    left: 309px; top: 665px; width: 581px; height: 381px;
    background: var(--paper);
  }
  .side-panel {
    position: absolute; left: 0; top: 0; width: 230px; height: 100%;
    background: var(--ink);
    display: flex; align-items: center; justify-content: center;
  }
  .side-name {
    color: var(--paper);
    font-weight: 500;
    font-size: 16px;
    letter-spacing: 1px;
    text-transform: uppercase;
    margin-top: -2px;
  }
  .back-name {
    position: absolute; left: 250px; width: 300px; top: 36px;
    text-align: center;
    color: var(--ink);
    font-weight: 500;
    font-size: 28px;
    line-height: 36px;
    letter-spacing: 1.5px;
    text-transform: uppercase;
  }

  .contact-list {
    position: absolute; right: 44px; top: 150px;
    list-style: none;
  }
  .contact-item {
    display: flex; align-items: flex-start; justify-content: flex-end;
    gap: 14px;
    margin-bottom: 7px;
    color: var(--ink);
    font-size: 12.5px;
    line-height: 18px;
    text-align: right;
  }
  .contact-item.address { line-height: 15px; margin-bottom: 9px; }
  .contact-item.address .icon { margin-top: 1px; }
  .icon {
    flex: none; width: 19px; height: 19px;
    border-radius: 50%;
    background: var(--ink);
    display: flex; align-items: center; justify-content: center;
  }
  .icon svg { width: 11px; height: 11px; }
</style>
</head>
<body>
<main class="canvas">

  <section class="card card-front" aria-label="Card front">
    <h1 class="front-name">TR Hair Studio</h1>
  </section>

  <section class="card card-back" aria-label="Card back">
    <div class="side-panel">
      <span class="side-name">TR Hair Studio</span>
    </div>

    <h2 class="back-name">TR Hair Studio</h2>

    <ul class="contact-list">
      <li class="contact-item address">
        <span>2751 Birchfield Rd.E. Mississauga,<br>ON L7P3K2</span>
        <span class="icon">
          <svg viewBox="0 0 12 12"><path d="M6 1 L11 5.5 H9.5 V11 H7 V8 H5 V11 H2.5 V5.5 H1 Z" fill="#fff"/></svg>
        </span>
      </li>
      <li class="contact-item">
        <span>905 614-2870</span>
        <span class="icon">
          <svg viewBox="0 0 12 12"><path d="M2.5 1 L4.5 1 L5.3 3.6 L4 4.6 C4.6 6 5.9 7.4 7.4 8 L8.4 6.7 L11 7.5 L11 9.5 C11 10.3 10.3 11 9.5 11 C5 10.7 1.3 7 1 2.5 C1 1.7 1.7 1 2.5 1 Z" fill="#fff"/></svg>
        </span>
      </li>
      <li class="contact-item">
        <span>trhairexample.ca</span>
        <span class="icon">
          <svg viewBox="0 0 12 12" fill="none" stroke="#fff" stroke-width="1"><circle cx="6" cy="6" r="4.8"/><ellipse cx="6" cy="6" rx="2" ry="4.8"/><line x1="1.2" y1="6" x2="10.8" y2="6"/></svg>
        </span>
      </li>
      <li class="contact-item">
        <span>tr.hairstudio</span>
        <span class="icon" aria-hidden="true"></span>
      </li>
      <li class="contact-item">
        <span>@TR_HairStudio</span>
        <span class="icon" aria-hidden="true"></span>
      </li>
    </ul>
  </section>

</main>
</body>
</html>
```